New Television Homescreen Template

We need a new default homescreen design for our televisions. This should reflect our company branding. My company is called Wellward Systems, WSY for short. Our website is www.wsyq.com. We develop televisions and infotainment solutions for the healthcare industry. I am somewhat open to different color palettes but our company colors are blue, black, and white. Our design is constrained by the 9 buttons, however the design of the buttons can be changed. Also, there is a video box on the right side of the screen as shown, this design can also be changed.

Target Market(s)

Hospital Patients

Requirements
Must have
• PSD template.

```html
<!DOCTYPE html>
<html lang="en">
<head>
<meta charset="utf-8">
<title>Wellward Systems – Television Homescreen</title>
<link rel="stylesheet" href="https://fonts.googleapis.com/css2?family=Comfortaa:wght@300;400&family=Arimo:wght@700&family=Open+Sans:wght@400&display=swap">
<style>
  :root {
    --page-bg: #eef0f2;
    --screen-deep: #0b1e27;
    --screen-mid: #183746;
    --screen-glow: #2bd1c0;
    --white: #ffffff;
    --ink: #1c1f24;
    --brand-blue: #3aa9dc;
    --tag-magenta: #b63fb5;
    --tag-green: #6fcf2a;
    --tag-cyan: #39c6e0;
    --tag-pink: #d2567a;
    --tag-yellow: #e8e23a;
    --video-bg: #1e232c;
    --tile-welcome: #b01e2a;
    --tile-cable: #a9b84a;
    --tile-movies: #b18c2c;
    --tile-map: #2fc13a;
    --tile-portal: #1f6fc4;
    --tile-dining: #8a2fb0;
    --tile-phone: #c23a87;
    --tile-education: #4aaeb4;
    --tile-request: #26393f;
  }
  * { margin: 0; padding: 0; box-sizing: border-box; }
  html, body {
    width: 1200px; height: 1000px; overflow: hidden;
    background: var(--page-bg);
  }
  .homescreen {
    position: absolute; left: 0; top: 162px;
    width: 1200px; height: 675px; overflow: hidden;
    background: var(--screen-deep);
  }
  .backdrop {
    position: absolute; inset: 0;
    background:
      radial-gradient(ellipse 260px 160px at 1000px 560px, rgba(43,209,192,0.55), transparent 70%),
      radial-gradient(ellipse 320px 120px at 720px 600px, rgba(43,209,192,0.35), transparent 70%),
      radial-gradient(ellipse 200px 200px at 1150px 320px, rgba(80,200,220,0.30), transparent 70%),
      radial-gradient(circle 30px at 180px 60px, rgba(110,220,210,0.55), transparent 80%),
      linear-gradient(180deg, var(--screen-mid) 0%, #14323f 45%, #0f3a3c 75%, #123f3d 100%);
  }
  .tagline {
    position: absolute; left: 79px; top: 92px; width: 441px;
    text-align: center; color: var(--white);
    font-family: "Comfortaa", sans-serif; font-weight: 300;
    line-height: 34px;
  }
  .tagline .line { display: block; white-space: nowrap; }
  .t-sm { font-size: 18px; }
  .t-md { font-size: 31px; }
  .t-lg { font-size: 44px; }
  .magenta { color: var(--tag-magenta); }
  .green { color: var(--tag-green); }
  .cyan { color: var(--tag-cyan); }
  .pink { color: var(--tag-pink); }
  .yellow { color: var(--tag-yellow); }
  .video-panel {
    position: absolute; left: 79px; top: 270px; width: 441px; height: 248px;
    background: var(--video-bg);
  }
  .video-art { position: absolute; inset: 0; background: radial-gradient(ellipse 140px 120px at 50% 45%, #3a414c, var(--video-bg) 80%); }
  .play-button { position: absolute; left: 189px; top: 120px; }
  .brand-band {
    position: absolute; left: 0; top: 518px; width: 1200px; height: 157px;
    background: linear-gradient(90deg, rgba(255,255,255,0.97) 0%, rgba(255,255,255,0.92) 35%, rgba(230,245,245,0.55) 55%, rgba(255,255,255,0) 75%);
  }
  .brand {
    position: absolute; left: 152px; top: 538px;
    display: flex; align-items: center; gap: 10px;
  }
  .brand-mark { width: 16px; height: 16px; background: var(--brand-blue); }
  .brand-name {
    font-family: "Open Sans", sans-serif; font-weight: 400;
    font-size: 30px; color: var(--ink); letter-spacing: -0.3px;
  }
  .brand-motto {
    position: absolute; left: 338px; top: 586px;
    font-family: "Open Sans", sans-serif; font-size: 11px; color: var(--ink);
  }
  .menu {
    position: absolute; left: 664px; top: 194px;
    display: grid; grid-template-columns: repeat(3, 143px); grid-auto-rows: 94px;
    column-gap: 10px; row-gap: 18px;
  }
  .tile {
    display: flex; align-items: center; justify-content: center; text-align: center;
    border-radius: 4px; color: var(--white);
    font-family: "Arimo", sans-serif; font-weight: 700; font-size: 18px; line-height: 1.05;
    text-transform: uppercase;
    box-shadow: inset 0 1px 0 rgba(255,255,255,0.25), 0 2px 6px rgba(0,0,0,0.3);
    background-image: linear-gradient(180deg, rgba(255,255,255,0.12), rgba(0,0,0,0.08));
  }
  .tile-small { font-size: 15px; }
  .tile-welcome { background-color: var(--tile-welcome); font-size: 26px; letter-spacing: -1px; }
  .tile-cable { background-color: var(--tile-cable); }
  .tile-movies { background-color: var(--tile-movies); }
  .tile-map { background-color: var(--tile-map); }
  .tile-portal { background-color: var(--tile-portal); }
  .tile-dining { background-color: var(--tile-dining); }
  .tile-phone { background-color: var(--tile-phone); }
  .tile-education { background-color: var(--tile-education); }
  .tile-request { background-color: var(--tile-request); }
</style>
</head>
<body>
  <main class="homescreen">
    <div class="backdrop" role="img" aria-label="Blurred night city skyline with a lit bridge reflected in water"></div>

    <h1 class="tagline">
      <span class="line"><span class="t-sm magenta">Improving</span> <span class="t-md">people’s</span></span>
      <span class="line"><span class="t-md green">lives</span> <span class="t-sm">through</span> <span class="t-lg cyan">innovation</span></span>
      <span class="line"><span class="t-md">in research,</span> <span class="t-md pink" style="font-size:26px">education</span></span>
      <span class="line"><span class="t-md">and</span> <span class="t-lg yellow">patient care</span></span>
    </h1>

    <section class="video-panel">
      <div class="video-art" role="img" aria-label="Video thumbnail with a white leafy tree illustration"></div>
      <svg class="play-button" width="62" height="44" viewBox="0 0 62 44" aria-label="Play video">
        <rect x="0" y="0" width="62" height="44" rx="4" fill="#e8e8e8"/>
        <path d="M24 12 L42 22 L24 32 Z" fill="#2a8fc0"/>
      </svg>
    </section>

    <div class="brand-band"></div>
    <div class="brand">
      <span class="brand-mark"></span>
      <span class="brand-name">Wellward Systems</span>
    </div>
    <p class="brand-motto">improving patient care</p>

    <nav class="menu">
      <a class="tile tile-welcome">Welcome</a>
      <a class="tile tile-cable">Cable TV</a>
      <a class="tile tile-movies">Movies</a>
      <a class="tile tile-map">Campus<br>Map</a>
      <a class="tile tile-portal tile-small">Crestview<br>MyPortal</a>
      <a class="tile tile-dining">Dining<br>Options</a>
      <a class="tile tile-phone tile-small">Important<br>Phone<br>Numbers</a>
      <a class="tile tile-education tile-small">Patient<br>Education<br>Materials</a>
      <a class="tile tile-request">Request<br>Services</a>
    </nav>
  </main>
</body>
</html>
```